Ranger

council ranger companion animals act local government act impounding act noxious weed act

Industry/Entity Type

Government

Contact Information for Business Card

ranger merrindale shire council marcus Tindle email address marcus.tindle01 @quellnet.com ph 0473906251

Font styles to use
Sans Serif

Colors
ec2027

```html
<!DOCTYPE html>
<html lang="en">
<head>
<meta charset="utf-8">
<title>Ranger – Merrindale Shire Council business card</title>
<link rel="stylesheet" href="https://fonts.googleapis.com/css2?family=Cinzel:wght@400;700&family=Lato:wght@400;700&display=swap">
<style>
  :root {
    --brand-red: #ec2027;
    --band-red: #d0232a;
    --card-black: #131313;
    --card-black-light: #1e1e1e;
    --stage: #2a2a2a;
    --white: #ffffff;
  }
  html, body {
    margin: 0;
    padding: 0;
    width: 1200px;
    height: 1000px;
    overflow: hidden;
    background: var(--stage);
  }
  .stage {
    position: relative;
    width: 1200px;
    height: 1000px;
  }
  .business-card {
    position: absolute;
    left: 110px;
    top: 201px;
    width: 980px;
    height: 598px;
    border-radius: 26px;
    overflow: hidden;
    box-shadow: 0 18px 40px rgba(0, 0, 0, 0.55);
  }
  .card-texture {
    position: absolute;
    inset: 0;
    background: linear-gradient(160deg, var(--card-black-light) 0%, var(--card-black) 60%, #0c0c0c 100%);
  }
  .card-content {
    position: absolute;
    left: 0;
    top: 0;
    width: 100%;
    text-align: center;
  }
  .title-block {
    position: absolute;
    left: 280px;
    top: 92px;
    text-align: left;
  }
  .role-title {
    margin: 0;
    font-family: "Cinzel", serif;
    font-weight: 400;
    font-size: 104px;
    line-height: 1;
    color: var(--brand-red);
    letter-spacing: 1px;
  }
  .council-name {
    margin: 2px 0 0 4px;
    font-family: "Lato", sans-serif;
    font-weight: 400;
    font-size: 33px;
    line-height: 1;
    color: var(--white);
    text-transform: uppercase;
    letter-spacing: 0.5px;
  }
  .holder-name {
    position: absolute;
    left: 0;
    width: 100%;
    top: 268px;
    margin: 0;
    font-family: "Cinzel", serif;
    font-weight: 700;
    font-size: 42px;
    color: var(--brand-red);
    letter-spacing: 2px;
  }
  .contact-list {
    position: absolute;
    left: 0;
    width: 100%;
    top: 340px;
    margin: 0;
    padding: 0;
    list-style: none;
    font-family: "Lato", sans-serif;
    font-size: 29px;
    color: var(--white);
  }
  .contact-list li { margin-bottom: 18px; }
  .contact-label {
    font-weight: 700;
    color: var(--brand-red);
    margin-right: 6px;
  }
  .accent-line {
    position: absolute;
    left: 0;
    width: 100%;
    top: 476px;
    height: 12px;
    background: var(--white);
  }
  .accent-band {
    position: absolute;
    left: 0;
    width: 100%;
    top: 494px;
    bottom: 0;
    background: var(--band-red);
  }
</style>
</head>
<body>
  <main class="stage">
    <section class="business-card">
      <div class="card-texture" role="img" aria-label="Dark carbon fibre texture"></div>
      <div class="card-content">
        <div class="title-block">
          <h1 class="role-title">Ranger</h1>
          <p class="council-name">Merrindale Shire Council</p>
        </div>
        <h2 class="holder-name">Marcus Tindle</h2>
        <ul class="contact-list">
          <li><span class="contact-label">P:</span>0473906251</li>
          <li><span class="contact-label">E:</span>marcus.tindle01@quellnet.com</li>
        </ul>
      </div>
      <div class="accent-line"></div>
      <div class="accent-band"></div>
    </section>
  </main>
</body>
</html>
```